Window Perf design with eadership quotes

I am wanting to create a window perf that covers windows in a conference room. I have included a picture of the windows. Each window is 26 1/2 inches by 92 inches. I have also included several other pictures to give an example of how I would like the Quotes to look.

Some Quotes I would like to use
1. Your Future is created by what you do today not tomorrow.
2. The answer is Yes
3. People don't care how much you know until they know how much you care.
4. Treat employees like they make a difference and they will.
5. Don't follow the crowd, Let the crowd follow you.
6. Treat people as if they were what they ought to be , and help them become what they are capable of being.
7. Leadership is not a title, its a behavior. LIVE IT
8. We make a living by what we get, We make a life by what we give.
9. Success is not final, failure is not fatal: it is courage to continue that counts.
10. The best way to predict your future is to create it.
11. The supreme quality of leadership is Integrity.
12. Whatever you are, Be a good one

Quotes

• I am imore interested in how this looks rather than including all of the quotes. I also ant this to be a solid background design for privacy.

```html
<!DOCTYPE html>
<html lang="en">
<head>
<meta charset="utf-8">
<title>Your Future Is Created By What You Do Today – Window Perf Panel</title>
<link rel="stylesheet" href="https://fonts.googleapis.com/css2?family=Oswald:wght@600;700&display=swap">
<style>
  :root {
    --panel-black: #000000;
    --gear-light: #e6e6e6;
    --gear-mid: #8a8a8a;
    --gear-dark: #2a2a2a;
    --quote-white: #ffffff;
  }
  html, body {
    margin: 0;
    padding: 0;
    width: 1200px;
    height: 4162px;
    overflow: hidden;
    background: var(--panel-black);
  }
  .window-panel {
    position: relative;
    width: 1200px;
    height: 4162px;
    background: var(--panel-black);
    overflow: hidden;
  }
  .gear-field {
    position: absolute;
    left: 0;
    width: 1200px;
  }
  .gear-field--top {
    top: 0;
    height: 1300px;
    background:
      linear-gradient(180deg, rgba(0,0,0,0) 0%, rgba(0,0,0,0) 70%, var(--panel-black) 100%),
      repeating-linear-gradient(180deg, var(--gear-light) 0px, var(--gear-mid) 140px, var(--gear-dark) 300px, var(--gear-light) 420px);
  }
  .gear-field--bottom {
    top: 2740px;
    height: 1422px;
    background:
      linear-gradient(0deg, rgba(0,0,0,0) 0%, rgba(0,0,0,0) 75%, var(--panel-black) 100%),
      repeating-linear-gradient(180deg, var(--gear-light) 0px, var(--gear-mid) 150px, var(--gear-dark) 310px, var(--gear-light) 440px);
  }
  .quote {
    position: absolute;
    left: 0;
    top: 0;
    width: 1200px;
    height: 4162px;
  }
  .quote__line {
    font-family: "Oswald", "Arial Narrow", sans-serif;
    font-weight: 600;
    fill: var(--quote-white);
    text-transform: uppercase;
  }
  .quote__line--hero {
    font-weight: 700;
  }
</style>
</head>
<body>
  <main class="window-panel">
    <div class="gear-field gear-field--top" role="img" aria-label="Pattern of interlocking grey and white gears with black centres"></div>

    <svg class="quote" viewBox="0 0 1200 4162" xmlns="http://www.w3.org/2000/svg" aria-label="Your future is created by what you do today, not tomorrow">
      <text class="quote__line" x="104" y="1613" font-size="196" textLength="1006" lengthAdjust="spacingAndGlyphs">Your Future</text>
      <text class="quote__line" x="104" y="1855" font-size="238" textLength="1006" lengthAdjust="spacingAndGlyphs">Is Created</text>
      <text class="quote__line" x="118" y="2011" font-size="140" textLength="986" lengthAdjust="spacingAndGlyphs">By What You Do</text>
      <text class="quote__line quote__line--hero" x="104" y="2358" font-size="356" textLength="1000" lengthAdjust="spacingAndGlyphs">Today</text>
      <text class="quote__line" x="104" y="2566" font-size="174" textLength="1006" lengthAdjust="spacingAndGlyphs">Not Tomorrow</text>
    </svg>

    <div class="gear-field gear-field--bottom" role="img" aria-label="Pattern of interlocking grey and white gears with black centres"></div>
  </main>
</body>
</html>
```